Business card Zottelgarten

Business card is for a self-employed dog trainer with own dog school. Name and logo of the dog school are available. Color specifications as well. The design should be classy and minimalist, but also modern. An already existing idea would be: Front: Only the logo Back: Contact data

Font styles to use
Serif
Sans Serif
Other font styles liked:
• Trajan Pro

Colors
f78f20

Requirements
Must have
• Name: Margit Wendler-Rasch Title: Dipl. Dog Trainer Contain my logo Follow my font and color preferences (see files)

```html
<!DOCTYPE html>
<html lang="en">
<head>
<meta charset="utf-8">
<title>Zottelgarten Business Card</title>
<link rel="stylesheet" href="https://fonts.googleapis.com/css2?family=Cinzel:wght@400&family=Roboto+Condensed:wght@700&family=Roboto:wght@400&display=swap">
<style>
  :root {
    --stage: #2b2b2b;
    --card-white: #f1f1ef;
    --brown: #7b6656;
    --brown-line: #6f5b4c;
    --ink-light: #ffffff;
    --ink-soft: #f3ece6;
  }
  html, body {
    margin: 0;
    padding: 0;
    width: 1200px;
    height: 960px;
    overflow: hidden;
    background: var(--stage);
  }
  .stage { position: relative; width: 1200px; height: 960px; }

  .card {
    position: absolute;
    width: 600px;
    height: 342px;
    background: var(--card-white);
    box-shadow: 0 2px 6px rgba(0,0,0,0.5);
  }
  .card--contact { left: 314px; top: 113px; }
  .card--brand { left: 311px; top: 472px; }

  .contact-frame {
    position: absolute;
    left: 8px; top: 8px; right: 8px; bottom: 8px;
    border: 2px solid var(--brown-line);
  }
  .contact-panel {
    position: absolute;
    left: 13px; top: 13px; right: 13px; bottom: 13px;
    background: var(--brown);
  }

  .person {
    position: absolute;
    right: 317px;
    top: 147px;
    text-align: right;
    color: var(--ink-light);
  }
  .person__name {
    margin: 0;
    font-family: "Roboto Condensed", "Arial Narrow", sans-serif;
    font-weight: 700;
    font-size: 27px;
    line-height: 32px;
    letter-spacing: 0.2px;
  }
  .person__title {
    margin: 0;
    font-family: "Roboto", Arial, sans-serif;
    font-size: 15px;
    line-height: 20px;
    letter-spacing: 0.6px;
    color: var(--ink-soft);
  }

  .divider {
    position: absolute;
    left: 309px;
    top: 92px;
    width: 1px;
    height: 156px;
    background: linear-gradient(to bottom, rgba(255,255,255,0), rgba(255,255,255,0.95) 30%, rgba(255,255,255,0.95) 70%, rgba(255,255,255,0));
  }

  .details {
    position: absolute;
    left: 338px;
    top: 98px;
    font-family: "Roboto", Arial, sans-serif;
    font-size: 15px;
    line-height: 19px;
    color: var(--ink-light);
  }
  .details__address { margin: 0 0 10px; }
  .details__list { list-style: none; margin: 0; padding: 0; }
  .details__item { display: flex; align-items: center; height: 19px; }
  .details__icon { width: 14px; height: 14px; margin-right: 9px; fill: var(--ink-light); }

  .brand {
    position: absolute;
    left: 0; right: 0; top: 80px;
    text-align: center;
  }
  .brand__dot {
    display: block;
    margin: 0 auto;
    width: 138px;
    height: 138px;
    border-radius: 50%;
    background: var(--brown);
  }
  .brand__name {
    margin: 14px 0 0;
    font-family: "Cinzel", "Trajan Pro", serif;
    font-weight: 400;
    font-size: 31px;
    line-height: 34px;
    letter-spacing: 1px;
    color: var(--brown);
  }
  .brand__web {
    margin: 0;
    font-family: "Cinzel", serif;
    font-size: 9px;
    line-height: 11px;
    letter-spacing: 4.2px;
    color: var(--brown);
  }
</style>
</head>
<body>
<main class="stage">
  <section class="card card--contact">
    <div class="contact-frame"></div>
    <div class="contact-panel"></div>

    <div class="person">
      <h1 class="person__name">MARGIT WENDLER-RASCH</h1>
      <p class="person__title">DIPL. DOG TRAINER</p>
    </div>

    <div class="divider"></div>

    <div class="details">
      <p class="details__address">4218 Larchwood Road<br>Millbrook, Vermont 52817</p>
      <ul class="details__list">
        <li class="details__item">
          <svg class="details__icon" viewBox="0 0 16 16" aria-hidden="true"><path d="M3.6 1.5l2.3 2.3c.4.4.4 1 0 1.4L4.7 6.4c.9 2 2.5 3.6 4.9 4.9l1.2-1.2c.4-.4 1-.4 1.4 0l2.3 2.3c.4.4.4 1 0 1.4l-1.3 1.3C10.5 16 0 5.5 1 2.8l1.2-1.3c.4-.4 1-.4 1.4 0z"/></svg>
          614 270 3391
        </li>
        <li class="details__item">
          <svg class="details__icon" viewBox="0 0 16 16" aria-hidden="true"><path d="M5 0h6c.8 0 1.5.7 1.5 1.5v13c0 .8-.7 1.5-1.5 1.5H5c-.8 0-1.5-.7-1.5-1.5v-13C3.5.7 4.2 0 5 0zm0 2v10.5h6V2H5zm3 11.3a.9.9 0 100 1.8.9.9 0 000-1.8z"/></svg>
          852 719 4406
        </li>
        <li class="details__item">
          <svg class="details__icon" viewBox="0 0 16 16" aria-hidden="true"><path d="M4 1h8v4H4zM1 6h14v6h-3v3H4v-3H1zm4 4v3.5h6V10z"/></svg>
          437 508 2163
        </li>
        <li class="details__item">
          <svg class="details__icon" viewBox="0 0 16 16" aria-hidden="true"><path d="M1 3.5h14v9H1zm1.5 1.2v.4L8 8.8l5.5-3.7v-.4zm0 2.1v4.5h11V6.8L8 10.5z"/></svg>
          hello@zottelgarten.ch
        </li>
        <li class="details__item">
          <svg class="details__icon" viewBox="0 0 16 16" aria-hidden="true"><circle cx="8" cy="8" r="7"/><path d="M5 4.5c1.5.3 2 1.3 1.5 2.3s.5 1.7 1.5 1.9-.2 2.3.5 3.3M10.5 3.8c-.8.8-.4 1.8.6 2" stroke="#7b6656" stroke-width="1.2" fill="none"/></svg>
          www.zottelgarten.ch
        </li>
      </ul>
    </div>
  </section>

  <section class="card card--brand">
    <div class="brand">
      <span class="brand__dot" role="img" aria-label="Zottelgarten dog school emblem area"></span>
      <p class="brand__name">ZOTTELGARTEN</p>
      <p class="brand__web">WWW.ZOTTELGARTEN.CH</p>
    </div>
  </section>
</main>
</body>
</html>
```